Business cards for a high-end menswear store

I would like to come up with a design for our business cards.
Two different ones: one for general sales and one for the owner. It is a high-end menswear store.

Our address is: 4817 Morneau Boulevard, Montreal, QC, K7P4M2
phone number: 514-286-5937
insta: MAISONVERLAINE
Website: www.maisonverlaine.example
email (general card): info@maisonverlaine.example
email (owner): bastien@maisonverlaine.example

I have attached our logo in an ai and eps file format. You can see our old cards as well. I am looking for a modern and clean look.

Target Market(s)

High-End Clothing Market

Industry/Entity Type

Retail, Clothing, Luxury Clothing

Contact Information for Business Card

Address, Name, Email, Website, Social Info,

Font styles to use
Serif

Colors

Designer to choose colors to be used in the design.

Requirements
Must have
• Address, Name, Email, Website, Social Info,
Nice to have
• QR Code that brings you to the website

```html
<!DOCTYPE html>
<html lang="en">
<head>
<meta charset="utf-8">
<title>Maison Verlaine — Business Cards</title>
<link href="https://fonts.googleapis.com/css2?family=Montserrat:wght@400;500&display=swap" rel="stylesheet">
<style>
  :root {
    --page: #d9d9d9;
    --card: #221f1f;
    --ink: #ffffff;
    --silver: #bdbdbd;
    --shadow: rgba(0, 0, 0, 0.35);
  }
  * { margin: 0; padding: 0; box-sizing: border-box; }
  html, body {
    width: 1200px;
    height: 856px;
    overflow: hidden;
    background: var(--page);
    font-family: "Montserrat", sans-serif;
  }
  .sheet {
    position: relative;
    width: 1200px;
    height: 856px;
    display: flex;
    align-items: center;
    justify-content: center;
    gap: 60px;
  }
  .card {
    position: relative;
    width: 525px;
    height: 300px;
    background: var(--card);
    color: var(--ink);
    box-shadow: 0 18px 40px var(--shadow);
  }
  .wordmark {
    position: absolute;
    text-align: center;
    font-weight: 400;
    text-transform: uppercase;
    white-space: nowrap;
  }
  .card--front .wordmark {
    top: 62px;
    right: 44px;
    font-size: 20px;
    letter-spacing: 0.32em;
    line-height: 1.5;
    color: var(--ink);
  }
  .card--back .wordmark {
    top: 50%;
    left: 50%;
    transform: translate(-50%, -50%);
    font-size: 28px;
    letter-spacing: 0.34em;
    line-height: 1.5;
    color: var(--silver);
  }
  .contact {
    position: absolute;
    left: 34px;
    list-style: none;
    font-size: 13.5px;
    line-height: 1.45;
    letter-spacing: 0.01em;
  }
  .contact--place { top: 104px; }
  .contact--reach { bottom: 30px; }
  .contact li {
    display: flex;
    align-items: flex-start;
    gap: 10px;
    margin-bottom: 2px;
  }
  .contact--place li { margin-bottom: 6px; }
  .icon {
    flex: 0 0 14px;
    width: 14px;
    height: 14px;
    margin-top: 3px;
    fill: var(--ink);
  }
  .social-dot {
    flex: 0 0 14px;
    width: 14px;
    height: 14px;
    margin-top: 3px;
    border-radius: 50%;
    background: var(--ink);
  }
</style>
</head>
<body>
<main class="sheet">

  <section class="card card--front" aria-label="Business card, contact side">
    <div class="wordmark">Maison<br>Verlaine</div>

    <ul class="contact contact--place">
      <li><span class="social-dot" aria-hidden="true"></span><span>MAISONVERLAINE</span></li>
      <li>
        <svg class="icon" viewBox="0 0 14 14" aria-hidden="true"><path d="M7 0.5a4.8 4.8 0 0 0-4.8 4.8C2.2 9 7 13.5 7 13.5s4.8-4.5 4.8-8.2A4.8 4.8 0 0 0 7 0.5zm0 6.6a1.9 1.9 0 1 1 0-3.8 1.9 1.9 0 0 1 0 3.8z"/></svg>
        <span>4817 Morneau Boulevard<br>Montreal, QC, K7P4M2</span>
      </li>
    </ul>

    <ul class="contact contact--reach">
      <li>
        <svg class="icon" viewBox="0 0 14 14" aria-hidden="true"><path d="M3.2 1l2 2.6-1.2 1.5a8 8 0 0 0 4.9 4.9l1.5-1.2L13 10.8 11.4 13C5.6 12.6 1.4 8.4 1 2.6z"/></svg>
        <span>514-286-5937</span>
      </li>
      <li>
        <svg class="icon" viewBox="0 0 14 14" aria-hidden="true"><path d="M1 3h12v8H1zM1.6 3.5L7 8l5.4-4.5" fill="none" stroke="#fff" stroke-width="1.3"/></svg>
        <span>info@maisonverlaine.example</span>
      </li>
      <li>
        <svg class="icon" viewBox="0 0 14 14" aria-hidden="true"><path d="M1 3h12v8H1zM1.6 3.5L7 8l5.4-4.5" fill="none" stroke="#fff" stroke-width="1.3"/></svg>
        <span>bastien@maisonverlaine.example</span>
      </li>
      <li>
        <svg class="icon" viewBox="0 0 14 14" aria-hidden="true"><g fill="none" stroke="#fff" stroke-width="1.1"><circle cx="7" cy="7" r="5.9"/><ellipse cx="7" cy="7" rx="2.6" ry="5.9"/><path d="M1.1 7h11.8"/></g></svg>
        <span>www.maisonverlaine.example</span>
      </li>
    </ul>
  </section>

  <section class="card card--back" aria-label="Business card, brand side">
    <div class="wordmark">Maison<br>Verlaine</div>
  </section>

</main>
</body>
</html>
```